Valbrook Data Works

Our company is about IT hardwares and IT solutions. IT hardware such as PC, RAMS, storage and servers. IT solutions such as project management, BA. We are also selling new technology too.

Target Market(s)

Consumer, Small to Medium Business, Corporate

Requirements
Must have
• The business card must have the following:
• Name:
• Title:
• Contact Number:
• Email address:
• Website:
• Color: Must match the logo color upgrade

```html
<!DOCTYPE html>
<html lang="en">
<head>
<meta charset="utf-8">
<title>Valbrook Data Works – Business Card</title>
<link rel="stylesheet" href="https://fonts.googleapis.com/css2?family=Exo+2:wght@700;800&family=Arimo:wght@400;700&display=swap">
<style>
  :root {
    --backdrop: #2a2a2a;
    --card: #262626;
    --card-edge: #333333;
    --ink-light: #e9e9e9;
    --accent: #d48a2a;
    --muted: #cfcfcf;
  }
  * { box-sizing: border-box; margin: 0; padding: 0; }
  html, body {
    width: 1200px;
    height: 997px;
    overflow: hidden;
    background: var(--backdrop);
  }
  .canvas {
    position: relative;
    width: 1200px;
    height: 997px;
  }
  .card {
    position: absolute;
    width: 540px;
    height: 308px;
    background: var(--card);
    border: 1px solid var(--card-edge);
    border-radius: 18px;
    box-shadow: 0 14px 34px rgba(0,0,0,0.55);
  }
  .card--front { left: 330px; top: 130px; }
  .card--back  { left: 330px; top: 520px; }

  .wordmark {
    font-family: "Exo 2", sans-serif;
    font-weight: 800;
    color: var(--ink-light);
    text-transform: uppercase;
    letter-spacing: 1px;
    line-height: 1;
  }
  .card--front .brand {
    position: absolute;
    inset: 0;
    display: flex;
    align-items: center;
    justify-content: center;
    gap: 16px;
  }
  .brand-dot {
    width: 30px;
    height: 30px;
    border-radius: 50%;
    background: var(--accent);
  }
  .card--front .wordmark { font-size: 36px; }

  .card--back .wordmark {
    position: absolute;
    right: 46px;
    top: 52px;
    font-size: 30px;
  }
  .divider {
    position: absolute;
    left: 200px;
    right: 40px;
    top: 168px;
    height: 1px;
    background: var(--accent);
  }
  .website {
    position: absolute;
    right: 44px;
    top: 146px;
    font-family: "Arimo", sans-serif;
    font-size: 14px;
    letter-spacing: 1px;
    color: var(--accent);
  }
  .person {
    position: absolute;
    left: 40px;
    top: 152px;
    font-family: "Arimo", sans-serif;
  }
  .person-name {
    font-size: 18px;
    font-weight: 700;
    color: var(--accent);
    text-transform: uppercase;
  }
  .person-title {
    font-size: 15px;
    color: var(--ink-light);
    margin-top: 2px;
  }
  .contacts {
    position: absolute;
    left: 40px;
    top: 218px;
    list-style: none;
    font-family: "Arimo", sans-serif;
    font-size: 15px;
    color: var(--muted);
  }
  .contact {
    display: flex;
    align-items: center;
    gap: 10px;
    height: 24px;
  }
  .contact-icon {
    width: 16px;
    height: 16px;
    flex: none;
  }
</style>
</head>
<body>
<main class="canvas">

  <section class="card card--front" aria-label="Card front">
    <div class="brand">
      <span class="brand-dot"></span>
      <span class="wordmark">Valbrook Data Works</span>
    </div>
  </section>

  <section class="card card--back" aria-label="Card back">
    <div class="wordmark">Valbrook Data Works</div>
    <div class="website">www.valbrookdata.com</div>
    <div class="divider"></div>
    <div class="person">
      <div class="person-name">Dana Holloway</div>
      <div class="person-title">Director</div>
    </div>
    <ul class="contacts">
      <li class="contact">
        <svg class="contact-icon" viewBox="0 0 16 16" aria-hidden="true">
          <circle cx="8" cy="8" r="8" fill="var(--accent)"/>
          <path d="M5 4.5h2l.7 2-1.2.8a5 5 0 0 0 2.2 2.2l.8-1.2 2 .7v2a1 1 0 0 1-1 1A6.5 6.5 0 0 1 4 5.5a1 1 0 0 1 1-1z" fill="var(--card)"/>
        </svg>
        555.310.2047
      </li>
      <li class="contact">
        <svg class="contact-icon" viewBox="0 0 16 16" aria-hidden="true">
          <circle cx="8" cy="8" r="8" fill="var(--accent)"/>
          <rect x="5" y="3.5" width="6" height="9" rx="1.2" fill="var(--card)"/>
          <rect x="6.2" y="4.8" width="3.6" height="5" fill="var(--accent)"/>
        </svg>
        555.318.6621
      </li>
      <li class="contact">
        <svg class="contact-icon" viewBox="0 0 16 16" aria-hidden="true">
          <circle cx="8" cy="8" r="8" fill="var(--accent)"/>
          <rect x="4" y="5" width="8" height="6" rx="0.8" fill="var(--card)"/>
          <path d="M4.3 5.3 8 8.3l3.7-3" fill="none" stroke="var(--accent)" stroke-width="0.9"/>
        </svg>
        dana@valbrookdata.com
      </li>
    </ul>
  </section>

</main>
</body>
</html>
```